Tarvel Ridge LLC

Need Professional Business cards for New Investment Fund

Target Market(s)

High Quality investors

Industry/Entity Type

Financial

Contact Information for Business Card

Phone Number +1 555 284 6193
Name Pavel Orlinsky
Title Fund Manager
email po@FundTarvel.example
Website www.FundTarvel.example

Colors

Designer to choose colors to be used in the design.

Requirements
Must have
• Must have our Logo and all of the above. Must be made so lettering and loge can be raised

```html
<!DOCTYPE html>
<html lang="en">
<head>
<meta charset="utf-8">
<title>Tarvel Ridge LLC — Business Card</title>
<link rel="stylesheet" href="https://fonts.googleapis.com/css2?family=Open+Sans:wght@400;600&display=swap">
<style>
  :root {
    --backdrop: #2c3038;
    --card: #232323;
    --accent: #4fc43a;
    --muted: #3a3a3a;
  }
  html, body {
    margin: 0;
    padding: 0;
    width: 1200px;
    height: 900px;
    overflow: hidden;
    background: var(--backdrop);
    font-family: "Open Sans", Arial, sans-serif;
  }
  .canvas {
    width: 1200px;
    height: 900px;
    display: flex;
    flex-direction: column;
    align-items: center;
    justify-content: center;
    gap: 36px;
  }
  .card {
    position: relative;
    width: 700px;
    height: 400px;
    background: var(--card);
    border: 3px solid var(--accent);
    box-sizing: border-box;
    box-shadow: 0 14px 30px rgba(0,0,0,0.45);
    overflow: hidden;
  }
  .brand {
    position: absolute;
    display: flex;
    align-items: center;
    gap: 10px;
  }
  .brand-square {
    width: 14px;
    height: 14px;
    background: var(--accent);
  }
  .brand-name {
    color: var(--accent);
    font-weight: 600;
    font-size: 22px;
    letter-spacing: 0.5px;
    line-height: 1;
  }

  /* front */
  .front .brand { right: 56px; top: 150px; }
  .person-name {
    position: absolute;
    left: 56px;
    top: 148px;
    margin: 0;
    color: var(--accent);
    font-weight: 600;
    font-size: 20px;
    line-height: 1.2;
  }
  .divider {
    position: absolute;
    left: 56px;
    right: 56px;
    top: 184px;
    height: 3px;
    background: var(--accent);
  }
  .person-title {
    position: absolute;
    left: 56px;
    top: 196px;
    margin: 0;
    color: var(--accent);
    font-size: 14px;
    line-height: 1.3;
  }
  .contact-list {
    position: absolute;
    left: 56px;
    top: 246px;
    margin: 0;
    padding: 0;
    list-style: none;
    display: flex;
    flex-direction: column;
    gap: 14px;
  }
  .contact {
    display: flex;
    align-items: center;
    gap: 12px;
    color: var(--accent);
    font-size: 14px;
    line-height: 1.2;
  }
  .contact svg { width: 16px; height: 16px; flex: none; }

  /* back */
  .back-mark {
    position: absolute;
    left: 40px;
    top: -20px;
    width: 240px;
    height: 240px;
    background: var(--muted);
    opacity: 0.7;
  }
  .back .brand { right: 56px; bottom: 60px; }
</style>
</head>
<body>
<main class="canvas">
  <section class="card front" aria-label="Card front">
    <h1 class="person-name">Pavel Orlinsky</h1>
    <div class="brand"><span class="brand-square"></span><span class="brand-name">Tarvel Ridge LLC</span></div>
    <div class="divider"></div>
    <p class="person-title">Fund Manager</p>
    <ul class="contact-list">
      <li class="contact">
        <svg viewBox="0 0 16 16" aria-hidden="true"><rect x="2" y="1" width="12" height="14" rx="3" fill="var(--accent)"/><rect x="6" y="4" width="6" height="8" rx="1" fill="var(--card)"/></svg>
        <span>+1 555 284 6193</span>
      </li>
      <li class="contact">
        <svg viewBox="0 0 16 16" aria-hidden="true"><rect x="1" y="3" width="14" height="10" fill="none" stroke="var(--accent)" stroke-width="1.6"/><path d="M1 3 L8 9 L15 3" fill="none" stroke="var(--accent)" stroke-width="1.6"/></svg>
        <span>po@FundTarvel.example</span>
      </li>
      <li class="contact">
        <svg viewBox="0 0 16 16" aria-hidden="true"><g fill="none" stroke="var(--accent)" stroke-width="1.3"><circle cx="8" cy="8" r="6.5"/><ellipse cx="8" cy="8" rx="3" ry="6.5"/><path d="M1.5 8 H14.5 M2.5 4.5 H13.5 M2.5 11.5 H13.5"/></g></svg>
        <span>www.FundTarvel.example</span>
      </li>
    </ul>
  </section>

  <section class="card back" aria-label="Card back">
    <div class="back-mark" aria-hidden="true"></div>
    <div class="brand"><span class="brand-square"></span><span class="brand-name">Tarvel Ridge LLC</span></div>
  </section>
</main>
</body>
</html>
```